Estate Planning Attorney Postcard

We need a double-sided postcard for a mail advertising campaign. We already started the project ourselves, but would like a professional designer to finish it. We will upload the already started project. We would like the project to use some or all of the stock photos we included, and would like the postcard finished with a professional but inviting theme that will be mailed to households.

Advertising

```html
<!DOCTYPE html>
<html lang="en">
<head>
<meta charset="utf-8">
<title>Proper Estate Planning Might Help You</title>
<link rel="stylesheet" href="https://fonts.googleapis.com/css2?family=Russo+One&family=Encode+Sans+Semi+Condensed:wght@400;700&display=swap">
<style>
  :root {
    --page: #ffffff;
    --cream: #fff3dc;
    --peach: #fbd9a0;
    --orange: #f6a02c;
    --deep-orange: #ee8a1a;
    --ink: #111111;
    --text: #1b1b1b;
    --skin-light: #e2b79a;
    --skin-mid: #c08a6c;
    --skin-dark: #8f604a;
    --paper: #f4f4f4;
    --meadow-light: #d8c9a0;
    --meadow-green: #7f8f55;
    --frame: #ffffff;
  }
  * { box-sizing: border-box; margin: 0; padding: 0; }
  html, body { width: 1200px; height: 900px; overflow: hidden; background: var(--page); }
  .postcard {
    position: absolute; left: 67px; top: 102px; width: 1070px; height: 693px; overflow: hidden;
    background:
      radial-gradient(ellipse 380px 260px at 1010px 620px, rgba(246,160,44,.45), transparent 70%),
      radial-gradient(ellipse 300px 220px at 80px 520px, rgba(246,160,44,.55), transparent 70%),
      linear-gradient(120deg, var(--cream) 0%, var(--peach) 45%, var(--cream) 70%, var(--peach) 100%);
  }
  .swoosh { position: absolute; inset: 0; width: 100%; height: 100%; }
  .headline {
    position: absolute; left: 0; right: 0; top: 46px; text-align: center;
    font-family: "Russo One", sans-serif; font-size: 46px; line-height: 50px; letter-spacing: 0;
    color: var(--ink); text-transform: uppercase; white-space: nowrap;
    transform: scaleX(.88); transform-origin: 534px 0;
  }
  .dotted-rule {
    position: absolute; left: 50px; right: 55px; top: 101px; height: 7px;
    background: radial-gradient(circle, var(--orange) 3px, transparent 3.5px) 0 0 / 9.2px 7px repeat-x;
  }
  .hands-photo {
    position: absolute; left: 22px; top: 145px; width: 645px; height: 548px;
    border-radius: 46% 46% 8% 8% / 40% 40% 0 0;
    background:
      radial-gradient(ellipse 240px 120px at 330px 330px, rgba(244,244,244,.85), transparent 75%),
      radial-gradient(ellipse 170px 300px at 170px 250px, var(--skin-light), transparent 80%),
      radial-gradient(ellipse 170px 300px at 480px 250px, var(--skin-light), transparent 80%),
      linear-gradient(180deg, var(--skin-mid) 0%, var(--skin-light) 45%, var(--skin-mid) 80%, var(--skin-dark) 100%);
  }
  .family-photo {
    position: absolute; left: 180px; top: 442px; width: 322px; height: 228px;
    border: 8px solid var(--frame); transform: rotate(-2.5deg);
    background: linear-gradient(180deg, var(--meadow-green) 0%, #a3a66f 45%, var(--meadow-light) 70%, #c9b383 100%);
    box-shadow: 0 4px 10px rgba(0,0,0,.35);
  }
  .benefits {
    position: absolute; left: 675px; top: 128px; width: 380px; list-style: none;
    font-family: "Encode Sans Semi Condensed", sans-serif; font-size: 14.6px; line-height: 19px; color: var(--text);
    white-space: nowrap;
  }
  .benefits li { position: relative; margin-bottom: 19px; padding-left: 10px; }
  .benefits li::before {
    content: ""; position: absolute; left: 0; top: 6px; width: 5px; height: 5px; border-radius: 50%;
    background: var(--deep-orange);
  }
  .benefits strong { font-weight: 700; text-transform: uppercase; }
</style>
</head>
<body>
  <main class="postcard">
    <svg class="swoosh" viewBox="0 0 1070 693" aria-hidden="true">
      <path d="M560 0 C 760 200, 900 330, 1070 360 L1070 420 C 880 380, 720 240, 530 0 Z" fill="rgba(255,255,255,.35)"/>
      <path d="M1070 430 C 950 520, 900 620, 880 693 L1070 693 Z" fill="rgba(255,255,255,.4)"/>
      <path d="M640 250 C 760 330, 860 420, 1070 470 L1070 500 C 850 450, 740 360, 630 270 Z" fill="rgba(238,138,26,.25)"/>
    </svg>

    <h1 class="headline">Proper Estate Planning Might Help You!</h1>
    <div class="dotted-rule"></div>

    <div class="hands-photo" role="img" aria-label="Two open cupped hands holding a paper-cut chain of a family holding hands"></div>
    <div class="family-photo" role="img" aria-label="Photo of a multi-generation family walking together through a sunny meadow"></div>

    <ul class="benefits">
      <li><strong>A living trust</strong> can help <strong>avoid probate,</strong> a time<br>consuming and potentially expensive court process<br>that may be required without an estate plan</li>
      <li>An <strong>advance health care directive</strong> or <strong>power of<br>attorney</strong> can help <strong>prepare for health care<br>and financial decisions,</strong> which may be made<br>for you in a way you dislike if you become<br>incapacitated without proper planning</li>
      <li>An estate plan can also <strong>protect your children</strong>,<br>by ensuring that the person you choose will care for<br>them in the event of your untimely death, and that<br>your assets get distributed the way you decide,<br>rather than the way a judge might decide without<br>an estate plan</li>
      <li><strong>A special needs trust</strong> can help <strong>plan for<br>disabled children</strong>, by making sure their<br>long-term care is not adversely affected by your<br>death and their inheritance, which can wipe-out<br>any public benefits they receive</li>
      <li>Explore ways to <strong>protect your assets</strong> from<br>lawsuits, unsuccessful business ventures,<br>and failed relationships</li>
    </ul>
  </main>
</body>
</html>
```